Harborline Hire Business Card Design

Need business cards designed for our new equipment rental. We specialize in renting to landscape / tree professionals, contractors, Do-It-Yourself'ers and Around the home or office. Looking for a eye catching card. Landscape and construction should be the theme. The logo is attached, and you can see our colors from the logo. You can use whatever color goes with it ok.

Target Market(s)

First off Landscape and Tree Professional. Then contractors, Do-It-Yourself'ers and rentals for Around the home or office.

Industry/Entity Type

Business

Contact Information for Business Card

Eye catching background that blends landscaping with construction equipment

Requirements
Must have
• Name on Card will Be: Martin Kolbeck (Manager)
• My Direct Phone Number is: 352-817-3062
• martin@harborlinehire.com
• www.harborlinehire.com
• 4712 Willow Brook Lane,
• Dade City FL 33590
Nice to have
• Would be Nice to have these bullets on the Face of the card that does not have all my information.
• Serving:
• Landscape / Tree Professionals
• Contractors
• DYI'ers or say Do-It-Yourself'ers
• Maybe have serving small and centered above these bullets, and these 3 bullets along the bottom of the card. Ideas?

```html
<!DOCTYPE html>
<html lang="en">
<head>
<meta charset="utf-8">
<title>Harborline Hire – Business Card</title>
<link rel="stylesheet" href="https://fonts.googleapis.com/css2?family=Lato:wght@400;700;900&display=swap">
<style>
  :root {
    --navy: #0d3e66;
    --navy-deep: #0a3359;
    --amber: #f6bb63;
    --white: #ffffff;
    --ink: #163f66;
    --page: #e9ebee;
  }
  * { box-sizing: border-box; margin: 0; padding: 0; }
  html, body { width: 1200px; height: 880px; overflow: hidden; }
  body {
    background: var(--page);
    font-family: "Lato", sans-serif;
    display: flex;
    flex-direction: column;
    align-items: center;
    justify-content: center;
    gap: 24px;
  }
  .card {
    position: relative;
    width: 714px;
    height: 408px;
    border-radius: 22px;
    overflow: hidden;
    box-shadow: 0 6px 18px rgba(0,0,0,.18);
  }

  /* Front */
  .card--front { background: var(--navy); color: var(--white); }
  .front-brand {
    position: absolute; top: 140px; left: 0; right: 0;
    display: flex; align-items: center; justify-content: center; gap: 14px;
  }
  .brand-dot { width: 22px; height: 22px; border-radius: 50%; background: var(--amber); }
  .brand-name { font-weight: 900; font-size: 44px; letter-spacing: .5px; text-transform: uppercase; }
  .front-brand .brand-name { color: var(--white); }
  .served {
    position: absolute; bottom: 62px; left: 0; right: 0;
    text-align: center; font-size: 17px; line-height: 1.45; color: var(--white);
  }
  .served li { display: inline; list-style: none; margin: 0 8px; }
  .served li::before {
    content: ""; display: inline-block; width: 8px; height: 8px; border-radius: 50%;
    background: var(--amber); margin-right: 7px; vertical-align: middle;
  }
  .served .row { display: block; }

  /* Back */
  .card--back { background: var(--white); }
  .back-swoosh { position: absolute; inset: 0; width: 100%; height: 100%; }
  .person { position: absolute; top: 46px; right: 46px; text-align: right; }
  .person-name { color: var(--white); font-weight: 700; font-size: 24px; }
  .person-role { color: var(--amber); font-size: 16px; margin-top: 1px; }
  .back-brand {
    position: absolute; top: 232px; left: 36px;
    display: flex; align-items: center; gap: 10px;
  }
  .back-brand .brand-name { color: var(--navy); font-size: 32px; }
  .back-brand .brand-dot { width: 16px; height: 16px; }
  .rule { position: absolute; top: 302px; left: 36px; width: 640px; height: 1px; background: var(--amber); }
  .contacts {
    position: absolute; top: 318px; left: 36px; right: 38px;
    display: flex; align-items: flex-start; color: var(--ink); font-size: 15.5px;
  }
  .contact-group { padding: 0 18px; line-height: 1.6; }
  .contact-group:first-child { padding-left: 0; }
  .contact-group + .contact-group { border-left: 1px solid var(--amber); }
  .contact-line { display: flex; align-items: center; gap: 8px; white-space: nowrap; }
  .icon { width: 18px; height: 18px; flex: none; }
  .phone { font-size: 19px; }
</style>
</head>
<body>

  <section class="card card--front">
    <div class="front-brand">
      <span class="brand-dot"></span>
      <span class="brand-name">Harborline Hire</span>
    </div>
    <ul class="served">
      <span class="row"><li>Landscape / Tree Professionals</li><li>Contractors</li></span>
      <span class="row"><li>DYI'ers or say Do-It-Yourself'ers</li></span>
    </ul>
  </section>

  <section class="card card--back">
    <svg class="back-swoosh" viewBox="0 0 714 408" preserveAspectRatio="none" aria-hidden="true">
      <path d="M0 0 H714 V118 C520 110 250 140 0 210 Z" fill="var(--navy)"/>
      <path d="M0 210 C250 140 520 110 714 118 V136 C520 124 250 150 20 228 Z" fill="var(--amber)"/>
    </svg>

    <div class="person">
      <div class="person-name">Martin Kolbeck</div>
      <div class="person-role">Manager</div>
    </div>

    <div class="back-brand">
      <span class="brand-dot"></span>
      <span class="brand-name">Harborline Hire</span>
    </div>

    <div class="rule"></div>

    <div class="contacts">
      <div class="contact-group">
        <div class="contact-line phone">
          <svg class="icon" viewBox="0 0 20 20"><circle cx="10" cy="10" r="9" fill="none" stroke="var(--amber)" stroke-width="1.5"/><rect x="7" y="5" width="6" height="10" rx="1.2" fill="none" stroke="var(--amber)" stroke-width="1.4"/></svg>
          352-817-3062
        </div>
      </div>
      <div class="contact-group">
        <div class="contact-line">
          <svg class="icon" viewBox="0 0 20 20"><circle cx="10" cy="10" r="9" fill="var(--amber)"/><rect x="5" y="6.5" width="10" height="7" fill="none" stroke="#fff" stroke-width="1.2"/><path d="M5 6.5 L10 10.5 L15 6.5" fill="none" stroke="#fff" stroke-width="1.2"/></svg>
          martin@harborlinehire.com
        </div>
        <div class="contact-line">
          <svg class="icon" viewBox="0 0 20 20"><circle cx="10" cy="10" r="9" fill="var(--amber)"/><circle cx="10" cy="10" r="5" fill="none" stroke="#fff" stroke-width="1.2"/><path d="M5 10 H15 M10 5 C7.5 8 7.5 12 10 15 M10 5 C12.5 8 12.5 12 10 15" fill="none" stroke="#fff" stroke-width="1"/></svg>
          www.harborlinehire.com
        </div>
      </div>
      <div class="contact-group">
        <div class="contact-line">4712 Willow Brook Lane,</div>
        <div class="contact-line">Dade City FL 33590</div>
      </div>
    </div>
  </section>

</body>
</html>
```